Boom Way Hoist Service Business Cards

I need a business card for "Boom Way Hoist and Haulage"

Boomway2023@hoistmail.net

Hoist Works LLC, Boom Way Hoist and Haulage LLC

555.014.7260 | www.BOOMWAYHOISTS.example

Central Indiana & Northeast Ohio

(IN) 14820 Maple Lane Noblesville, IN 46000

(OH) 2450 Pell Street Akron, Ohio 44300

Colors
0094D4
00A9DD
6FCCEA
C7EBF8
E9F6FB
59FF00
82FF00
B8FF75
E3FFCB
F4FFEA
EE7325
F08F49
F5BC92
FAE3D3
FDF4ED
EB3D1F
EC4F4E
F09395
F8D3D4
FCEDEE
E54698
E96AAD
F1A4CE
F9D9EA
FCEFF6
A7469A
B969AE
D3A5CF
EDDBEB
F8F0F9

```html
<!DOCTYPE html>
<html lang="en">
<head>
<meta charset="utf-8">
<title>Boom Way Hoist and Haulage – Business Cards</title>
<link href="https://fonts.googleapis.com/css2?family=Archivo+Black&family=Open+Sans:wght@400;600&display=swap" rel="stylesheet">
<style>
  :root {
    --backdrop: #d6d6d6;
    --card: #1c1c1c;
    --card-deep: #141414;
    --pattern-light: #3a3a3a;
    --brand-green: #33cc33;
    --edge-green: #59ff00;
    --ink: #ffffff;
    --rule: #3b3b3b;
  }
  * { box-sizing: border-box; margin: 0; padding: 0; }
  html, body { width: 1200px; height: 800px; overflow: hidden; }
  body {
    background: var(--backdrop);
    display: flex;
    align-items: center;
    justify-content: center;
    gap: 40px;
    font-family: "Open Sans", sans-serif;
  }
  .card {
    position: relative;
    width: 540px;
    height: 310px;
    background: var(--card);
    border-bottom: 3px solid var(--edge-green);
    border-right: 3px solid var(--edge-green);
    overflow: hidden;
  }

  /* Front */
  .card-front { display: flex; }
  .brand-block {
    width: 215px;
    display: flex;
    flex-direction: column;
    justify-content: flex-end;
    padding: 0 0 48px 34px;
  }
  .brand-name {
    font-family: "Archivo Black", sans-serif;
    color: var(--ink);
    font-size: 36px;
    line-height: 1;
    letter-spacing: 1px;
    text-transform: uppercase;
  }
  .divider {
    width: 1px;
    background: var(--rule);
    margin: 30px 0 40px;
  }
  .details {
    flex: 1;
    padding: 30px 20px 0 22px;
    color: var(--ink);
  }
  .company-lines {
    font-family: "Archivo Black", sans-serif;
    text-transform: uppercase;
    line-height: 1.1;
    font-size: 15px;
    letter-spacing: 0.5px;
    margin-bottom: 14px;
  }
  .company-lines .primary { color: var(--brand-green); display: block; }
  .company-lines .secondary { color: var(--ink); display: block; }
  .contact-list { list-style: none; font-size: 12px; line-height: 1.55; margin-bottom: 10px; }
  .contact-list li { display: flex; align-items: center; gap: 7px; }
  .contact-list svg { width: 11px; height: 11px; flex: none; fill: var(--brand-green); }
  .region { color: var(--brand-green); font-size: 12.5px; margin-bottom: 4px; }
  .address { font-size: 12.5px; line-height: 1.45; margin-bottom: 6px; }

  /* Back */
  .card-back { background: var(--card-deep); }
  .pattern-fill {
    position: absolute; inset: 0;
    background: linear-gradient(120deg, var(--card-deep) 0%, #222 45%, var(--pattern-light) 100%);
  }
  .back-brand {
    position: absolute;
    right: 70px;
    bottom: 70px;
    display: flex;
    align-items: center;
    gap: 10px;
  }
  .back-brand .brand-mark { width: 12px; height: 12px; background: var(--brand-green); }
  .back-brand .brand-name { font-size: 26px; }
</style>
</head>
<body>
  <section class="card card-front" aria-label="Business card front">
    <div class="brand-block">
      <p class="brand-name">Boom<br>Way</p>
    </div>
    <div class="divider"></div>
    <div class="details">
      <h1 class="company-lines">
        <span class="primary">Hoist Works LLC</span>
        <span class="secondary">Boom Way Hoist and Haulage LLC</span>
      </h1>
      <ul class="contact-list">
        <li><svg viewBox="0 0 24 24" aria-hidden="true"><path d="M6.6 10.8a15.5 15.5 0 0 0 6.6 6.6l2.2-2.2c.3-.3.7-.4 1-.2 1.1.4 2.3.6 3.6.6.6 0 1 .4 1 1V20c0 .6-.4 1-1 1A17 17 0 0 1 3 4c0-.6.4-1 1-1h3.5c.6 0 1 .4 1 1 0 1.3.2 2.5.6 3.6.1.3 0 .7-.2 1z"/></svg>555.014.7260</li>
        <li><svg viewBox="0 0 24 24" aria-hidden="true"><path d="M2 5h20v14H2z M2 5l10 8 10-8" /></svg>Boomway2023@hoistmail.net</li>
        <li><svg viewBox="0 0 24 24" aria-hidden="true"><circle cx="12" cy="12" r="10"/></svg>www.BOOMWAYHOISTS.example</li>
      </ul>
      <p class="region">Central Indiana &amp; Northeast Ohio</p>
      <p class="address">(IN) 14820 Maple Lane Noblesville,<br>IN 46000</p>
      <p class="address">(OH) 2450 Pell Street Akron,<br>Ohio 44300</p>
    </div>
  </section>

  <section class="card card-back" aria-label="Business card back">
    <div class="pattern-fill" role="img" aria-label="Repeating tonal brand pattern in dark greys"></div>
    <div class="back-brand">
      <span class="brand-mark"></span>
      <p class="brand-name">Boom Way</p>
    </div>
  </section>
</body>
</html>
```